Tattoo Shop Business Card

I need a Business Card for the The Harbor Quill.

I'm thinking i want a double sided business card, really clean, very classy, one side the logo, and on the other my information. I'm pretty much open to anything, as long as its fun and captures class and elegance, while at the same time is edgy and tattooish.
I don't want your typical classic card. Add your own twist on it

Logo is attached to this brief

Please include:
Name
Position
Phone Number
Email
Website

Target Market(s)

I'm looking to capture potential clients for my tattoo shop so the card needs to be something they can fit in their wallet but they will also remember me when they see that card in there. My target audience is everyone over 18 that is intrigued by tattoos and piercings.

Industry/Entity Type

Business

Font styles to use
Serif

Colors

Designer to choose colors to be used in the design.

Requirements
Must have
• must be bold and something people will never forget

```html
<!DOCTYPE html>
<html lang="en">
<head>
<meta charset="utf-8">
<title>The Harbor Quill – Business Card</title>
<link rel="stylesheet" href="https://fonts.googleapis.com/css2?family=Roboto+Condensed:wght@400;700&display=swap">
<style>
  :root {
    --page-light: #ffffff;
    --page-edge: #dedede;
    --card-center: #eef4f5;
    --card-mid: #b9d8dc;
    --card-edge: #3e969f;
    --card-border: #5a8f95;
    --ink: #231f20;
  }
  * { margin: 0; padding: 0; box-sizing: border-box; }
  html, body {
    width: 1200px;
    height: 686px;
    overflow: hidden;
  }
  body {
    position: relative;
    background: radial-gradient(ellipse at 50% 45%, var(--page-light) 30%, var(--page-edge) 100%);
    font-family: "Roboto Condensed", "Arial Narrow", sans-serif;
    color: var(--ink);
  }
  .card {
    position: absolute;
    top: 191px;
    width: 544px;
    height: 303px;
    border: 1px solid var(--card-border);
    background: radial-gradient(ellipse 60% 62% at 50% 50%, var(--card-center) 0%, var(--card-mid) 55%, var(--card-edge) 100%);
  }
  .card--front { left: 60px; }
  .card--back { left: 616px; }

  .brand-name {
    position: absolute;
    left: 0;
    width: 100%;
    text-align: center;
    font-weight: 700;
    text-transform: uppercase;
    letter-spacing: 0.02em;
    line-height: 1;
    white-space: nowrap;
  }
  .card--front .brand-name {
    top: 122px;
    font-size: 46px;
  }
  .card--back .brand-name {
    top: 120px;
    font-size: 28px;
  }

  .contact-phone {
    position: absolute;
    left: 27px;
    top: 30px;
    font-size: 19px;
    font-weight: 400;
  }
  .holder-name {
    position: absolute;
    right: 45px;
    top: 14px;
    font-size: 42px;
    font-weight: 700;
    line-height: 1.1;
  }
  .contact-address {
    position: absolute;
    left: 0;
    width: 100%;
    top: 232px;
    text-align: center;
    font-size: 19px;
  }
  .contact-online {
    position: absolute;
    left: 0;
    width: 100%;
    top: 256px;
    text-align: center;
    font-size: 18px;
    white-space: nowrap;
  }
  .contact-online .web {
    font-size: 21px;
    margin-left: 8px;
  }
</style>
</head>
<body>
  <section class="card card--front" aria-label="Card front">
    <p class="brand-name">The Harbor Quill</p>
  </section>

  <section class="card card--back" aria-label="Card back">
    <p class="contact-phone">040 555 0192</p>
    <h1 class="holder-name">Marcus</h1>
    <p class="brand-name">The Harbor Quill</p>
    <p class="contact-address">Tähtikuja 4 C 00560 Helsinki</p>
    <p class="contact-online">
      <span class="email">the harbor quill@marcus.in</span>
      <span class="web">www.the harbor quill.in</span>
    </p>
  </section>
</body>
</html>
```